Business card for massage therapy company called Brook Fern Wellness

Need business card for massage therapy company called Brook Fern Wellness. Would like my logo on the front and the back of the card I have 3 options of logos and you can play with what looks better.

Would like this information displayed on the back of the card:

Marcus Ellery
Licensed Massage Therapist
321-555-0147
brookfern-example.com
brookfern_rest_

```html
<!DOCTYPE html>
<html lang="en">
<head>
<meta charset="utf-8">
<title>Brook Fern Wellness – Business Card</title>
<link href="https://fonts.googleapis.com/css2?family=Open+Sans:wght@300;400;600;700&display=swap" rel="stylesheet">
<style>
  :root {
    --page: #e6e6e4;
    --card: #fbfbfa;
    --card-shade: #eeeeeb;
    --olive: #6b7259;
    --tan: #c4936c;
    --ink: #3f3f3f;
  }
  * { margin: 0; padding: 0; box-sizing: border-box; }
  html, body {
    width: 1200px; height: 900px; overflow: hidden;
    background: var(--page);
    font-family: "Open Sans", sans-serif;
    color: var(--ink);
  }
  .canvas { position: relative; width: 1200px; height: 900px; }

  .card {
    position: absolute;
    width: 640px; height: 366px;
    background: var(--card);
    border-radius: 36px;
    overflow: hidden;
    box-shadow: 0 10px 28px rgba(0,0,0,0.12);
  }
  .card--info { left: 130px; top: 44px; }
  .card--brand { left: 430px; top: 490px; }

  /* brand lockup */
  .brand {
    position: absolute;
    display: flex; flex-direction: column; align-items: center;
    color: var(--olive);
    font-weight: 300;
    text-transform: uppercase;
    text-align: center;
  }
  .brand__dot {
    border: 1.5px solid var(--olive);
    border-radius: 50%;
  }
  .brand__name { line-height: 1.15; letter-spacing: 3px; }

  .card--info .brand { left: 30px; top: 70px; width: 250px; }
  .card--info .brand__dot { width: 84px; height: 84px; margin-bottom: 14px; }
  .card--info .brand__name { font-size: 27px; }

  .divider {
    position: absolute; left: 298px; top: 58px;
    width: 1px; height: 190px; background: var(--tan); opacity: 0.7;
  }

  .contact { position: absolute; left: 328px; top: 66px; }
  .contact__name {
    font-size: 21px; font-weight: 700; color: var(--olive);
    text-transform: uppercase; line-height: 1.1;
  }
  .contact__role { font-size: 16px; margin-top: 2px; }
  .contact__list { list-style: none; margin-top: 26px; font-size: 16px; }
  .contact__list li { display: flex; align-items: center; gap: 9px; margin-bottom: 6px; }
  .contact__icon { width: 15px; height: 15px; flex: none; }
  .contact__social-dot { width: 13px; height: 13px; border-radius: 50%; background: var(--ink); flex: none; margin: 0 1px; }

  .url-band {
    position: absolute; left: 0; top: 286px;
    width: 560px; height: 30px;
    background: var(--olive);
    color: #fff;
    font-size: 15px; letter-spacing: 8.5px;
    display: flex; align-items: center; justify-content: center;
    padding-left: 40px;
  }
  .band-accent {
    position: absolute; left: 578px; top: 252px;
    width: 62px; height: 30px; background: var(--tan);
  }
  .band-seal {
    position: absolute; left: 530px; top: 254px;
    width: 58px; height: 58px; border-radius: 50%;
    background: var(--card);
    border: 1.5px solid var(--olive);
  }

  /* back */
  .leaf-decor {
    position: absolute; inset: 0;
    background: linear-gradient(160deg, var(--card) 0%, var(--card) 45%, var(--card-shade) 100%);
  }
  .card--brand .brand { left: 0; right: 0; top: 88px; margin: 0 auto; width: 360px; }
  .card--brand .brand__dot { width: 100px; height: 100px; margin-bottom: 16px; }
  .card--brand .brand__name { font-size: 32px; }
</style>
</head>
<body>
<main class="canvas">

  <section class="card card--info" aria-label="Card contact side">
    <div class="brand">
      <span class="brand__dot"></span>
      <span class="brand__name">Brook Fern<br>Wellness</span>
    </div>
    <span class="divider"></span>
    <div class="contact">
      <p class="contact__name">Marcus Ellery</p>
      <p class="contact__role">Licensed Massage Therapist</p>
      <ul class="contact__list">
        <li>
          <svg class="contact__icon" viewBox="0 0 24 24" aria-hidden="true">
            <path fill="#3f3f3f" d="M6.6 10.8a15.1 15.1 0 0 0 6.6 6.6l2.2-2.2c.3-.3.7-.4 1-.2 1.1.4 2.3.6 3.6.6.6 0 1 .4 1 1V20c0 .6-.4 1-1 1C10.6 21 3 13.4 3 4c0-.6.4-1 1-1h3.5c.6 0 1 .4 1 1 0 1.3.2 2.5.6 3.6.1.3 0 .7-.2 1z"/>
          </svg>
          321-555-0147
        </li>
        <li><span class="contact__social-dot"></span>brookfern_rest_</li>
      </ul>
    </div>
    <span class="band-accent"></span>
    <div class="url-band">brookfern-example.com</div>
    <span class="band-seal"></span>
  </section>

  <section class="card card--brand" aria-label="Card brand side">
    <div class="leaf-decor" role="img" aria-label="Faint sage leaf sprig decoration across the card"></div>
    <div class="brand">
      <span class="brand__dot"></span>
      <span class="brand__name">Brook Fern<br>Wellness</span>
    </div>
  </section>

</main>
</body>
</html>
```